R&T Cleanwave Stripping Business Card

We are in need of a business card design for our new Texas based company called 'R&T Cleanwave Stripping'. Our new innovative mobile media blasting service utilizes recycled material and a new water based process that eliminates all dust (i.e. as apposed to the old sand blasting format). Our 'advanced surface preparation' service targets multiple industries such as automotive, Industrial, marine and structural (graffiti removal). We would like to see the design include a recycling type logo or concept that utilizes colors such as black, various shades of green, some white, yellow and/or grey (e.g. perhaps a blackish background). The final design should look simple and professional and should clearly communicate the environmentally friendly approach through logo or design (i.e. Eco-Friendly, Go Green or Blast Green methodologies). Thank you in advance!
Updates

Please pardon any inconvenience. We have decided to pursue a two sided business card. All original information/designs requirements remains the same for the front. However, we would like back of the card to state the following: "We bring the power of Hydroveil Media Scouring equipment to your location. We can remove any coating from any surface. Bullets include: Paint Stripping, Auto Restoration, Graffiti Removal, Black Walls & Stone, Concrete, Boats, Iron Fences, Tractors & Trailers, Pools & Fountains, Wood Restoration.

Industry/Entity Type

Recycling

Contact Information for Business Card

R&T Cleanwave Stripping, LLC - Gordon Pelly, MBA, PMP - cell: 915-382-6091, office: 915-627-8853 - gpelly@rtcleanwavestripping.com - CEO/Founder

Requirements
Must have
• Recycle or environmentally friendly logos or design.
Nice to have
• Business oriented design with an aggressive look. Also, if possible would like to see R&T incorporated into the design or logo. Please note that we have decided to add the option of adding details to the back of the card (2 sided). The front should contain the logo/design and the back should have the following details listed: "We bring the power of Hydroveil Media Scouring equipment to your location. We can remove any coating from any surface. Bullets include: Paint Stripping, Auto Restoration, Graffiti Removal, Black Walls & Stone, Concrete, Boats, Iron Fences, Tractors & Trailers, Pools & Fountains, Wood Restoration.

```html
<!DOCTYPE html>
<html lang="en">
<head>
<meta charset="utf-8">
<title>R&amp;T Cleanwave Stripping – Business Card</title>
<link rel="stylesheet" href="https://fonts.googleapis.com/css2?family=Lato:wght@400;700;900&display=swap">
<style>
  :root {
    --stage: #e9e9e6;
    --card-dark: #2a2a2a;
    --card-light: #ffffff;
    --green: #45a347;
    --ink: #262626;
    --white: #ffffff;
  }
  * { box-sizing: border-box; margin: 0; padding: 0; }
  html, body {
    width: 1200px; height: 1000px; overflow: hidden;
    background: var(--stage);
    font-family: 'Lato', sans-serif;
  }
  .stage {
    width: 1200px; height: 1000px;
    display: flex; flex-direction: column; align-items: center; justify-content: center;
    gap: 40px;
  }
  .card {
    width: 770px; height: 440px; position: relative; overflow: hidden;
    box-shadow: 0 6px 18px rgba(0,0,0,.18);
  }
  /* Back */
  .card--back {
    background: var(--card-dark); color: var(--white);
    display: flex; flex-direction: column; align-items: center; padding-top: 86px;
  }
  .brand {
    display: flex; align-items: center; gap: 14px;
    font-weight: 900; letter-spacing: .5px;
  }
  .brand__dot { border-radius: 50%; background: var(--green); flex: none; }
  .card--back .brand { font-size: 38px; color: var(--white); }
  .card--back .brand__dot { width: 34px; height: 34px; }
  .tagline {
    margin-top: 70px; color: var(--green); font-size: 17px; line-height: 1.35; text-align: center;
  }
  .services {
    list-style: none; margin-top: 14px; width: 640px;
    display: flex; flex-wrap: wrap; justify-content: center; gap: 4px 20px;
    font-size: 16px;
  }
  .services li::before {
    content: ""; display: inline-block; width: 7px; height: 7px; border-radius: 50%;
    background: var(--green); margin-right: 7px; vertical-align: middle;
  }
  /* Front */
  .card--front { background: var(--card-light); color: var(--ink); }
  .card--front .brand {
    position: absolute; left: 56px; top: 168px; width: 320px;
    font-size: 30px; line-height: 1.2; color: var(--ink); gap: 14px;
  }
  .card--front .brand__dot { width: 30px; height: 30px; }
  .person { position: absolute; left: 412px; top: 120px; }
  .person__name { color: var(--green); font-size: 25px; font-weight: 400; }
  .person__creds { font-size: 19px; margin-left: 6px; }
  .person__role { font-size: 19px; margin-top: 4px; }
  .contacts { list-style: none; position: absolute; left: 416px; top: 214px; font-size: 20px; }
  .contacts li { display: flex; align-items: center; gap: 12px; height: 30px; }
  .contacts svg { width: 20px; height: 20px; fill: var(--green); flex: none; }
  .footer-band { position: absolute; left: 0; bottom: 0; width: 100%; height: 28px; background: var(--card-dark); }
  .footer-band svg { position: absolute; right: 0; top: 0; }
</style>
</head>
<body>
<main class="stage">
  <section class="card card--back" aria-label="Card back">
    <div class="brand"><span class="brand__dot"></span>R&amp;T Cleanwave Stripping, LLC</div>
    <p class="tagline">We bring the power of Hydroveil Media Scouring Equipment to your location.<br>We can remove any coating from any surface.</p>
    <ul class="services">
      <li>Paint Stripping</li><li>Auto Restoration</li><li>Graffiti Removal</li><li>Black Walls &amp; Stones</li>
      <li>Concrete</li><li>Boats</li><li>Iron Fences</li><li>Tractors &amp; Trailers</li>
      <li>Pools &amp; Fountains</li><li>Wood Restoration</li>
    </ul>
  </section>

  <section class="card card--front" aria-label="Card front">
    <div class="brand"><span class="brand__dot"></span><span>R&amp;T Cleanwave<br>Stripping, LLC</span></div>
    <div class="person">
      <p class="person__name">Gordon Pelly,<span class="person__creds">MBA, PMP</span></p>
      <p class="person__role">CEO/Founder</p>
    </div>
    <ul class="contacts">
      <li><svg viewBox="0 0 24 24" aria-hidden="true"><path d="M6.6 10.8a15.2 15.2 0 0 0 6.6 6.6l2.2-2.2a1 1 0 0 1 1-.25 11.4 11.4 0 0 0 3.6.57 1 1 0 0 1 1 1V20a1 1 0 0 1-1 1A17 17 0 0 1 3 4a1 1 0 0 1 1-1h3.5a1 1 0 0 1 1 1c0 1.250.2 2.450.57 3.570a1 1 0 0 1-.25 1z"/></svg>915-627-8853</li>
      <li><svg viewBox="0 0 24 24" aria-hidden="true"><path d="M8 1h8a2 2 0 0 1 2 2v18a2 2 0 0 1-2 2H8a2 2 0 0 1-2-2V3a2 2 0 0 1 2-2zm0 3v14h8V4zm4 15.5a1 1 0 1 0 0 2 1 1 0 0 0 0-2z"/></svg>915-382-6091</li>
      <li><svg viewBox="0 0 24 24" aria-hidden="true"><path d="M2 5h20v14H2zm2 2v.4l8 5 8-5V7zm0 2.7V17h16V9.7l-8 5z"/></svg>gpelly@rtcleanwavestripping.com</li>
    </ul>
    <div class="footer-band">
      <svg width="280" height="28" viewBox="0 0 280 28" aria-hidden="true"><polygon points="8,28 20,0 280,0 280,28" fill="var(--green)"/></svg>
    </div>
  </section>
</main>
</body>
</html>
```